Learning platform for primary and secondary schools needs a new design

We need to restyle the website: www.pennaboschetto.org.
We are developing new functionalities that will enable to turn the platform in an interactive e-learning center for teachers, parents and pupils. Our target is providing contents and learning methods for primary and secondary school.
We want to give a new structure to the homepage and all menu sections and to find a new design that facilitates users to orientate themselves. We love our main picture and we would like to emphasize it. We like our logo and we don't want to change it.
The homepage should fulfil three main tasks:
- welcome visitors;
- encourage visitors to explore three areas of free contents: learning (scopri), experimenting (esperimenti), cooking (ricette)
- convert visitors in logged users (users can register as teachers, parents or students).
We also need a new design for:
- log-in page,
- slideshow,
- galleries of pictures,
- blog page,
- newsletter.
If you have any questions, do not hesitate to contact me.
Good job!
Giulia
Updates
Hi guys,
First of all I'd like to say thanks to all designers that submitted their ideas.
Up to now I didn't find any design that really convinced me, that's why I decided to share with you a design idea that could make easier your job (please see again the project briefing). I can't wait to see your new designs!
Good job
Ciao
Giuliabetta
Hi guys,
I would like to thank you for all your wonderful design proposals. We have just launched a friends and family voting pool to help us in getting the final decision. We'll let you know the result as soon as possible within tomorrow.
Ciao
Giuliabetta
Target Market(s)
Italian teachers, parents and students attending primary and secondary school
Industry/Entity Type
Cooking
Look and feel
Each slider illustrates characteristics of the customer's brand and the style your logo design should communicate.

```html
<!DOCTYPE html>
<html lang="en">
<head>
<meta charset="utf-8">
<title>PennaBoschetto – The taste of knowledge</title>
<link href="https://fonts.googleapis.com/css2?family=Roboto:wght@300;400;500&display=swap" rel="stylesheet">
<style>
  :root {
    --orange: #f7890c;
    --green: #8dc63f;
    --dark: #2e2e2e;
    --dark-2: #3a3a3a;
    --field-border: #5a5a5a;
    --text: #333333;
    --muted: #555555;
    --soft: #f7f7f7;
    --line: #e6e6e6;
    --sky-top: #63c3ee;
    --sky: #a8dcf4;
    --white: #ffffff;
  }
  * { box-sizing: border-box; margin: 0; padding: 0; }
  html, body { width: 758px; height: 1200px; overflow: hidden; }
  body { position: relative; background: var(--white); font-family: 'Roboto', Arial, sans-serif; color: var(--text); }
  .abs { position: absolute; }

  /* header */
  .brand { left: 108px; top: 60px; display: flex; align-items: center; gap: 6px; }
  .brand-dot { width: 18px; height: 18px; border-radius: 50%; background: var(--orange); }
  .brand-name { font-size: 21px; font-weight: 500; color: var(--orange); }
  .phone { left: 506px; top: 12px; display: flex; align-items: center; gap: 6px; color: var(--green); font-size: 16px; }
  .account { left: 396px; top: 54px; font-size: 8px; color: var(--text); }
  .account span { margin: 0 4px; }
  .icon-row { left: 485px; top: 47px; display: flex; gap: 10px; }
  .icon-ring { width: 24px; height: 24px; border: 1.5px solid var(--orange); border-radius: 50%; display: flex; align-items: center; justify-content: center; }
  .icon-ring .pip { width: 8px; height: 8px; border-radius: 50%; background: var(--orange); }
  .main-nav { left: 279px; top: 88px; width: 370px; height: 40px; background: var(--dark); display: flex; }
  .main-nav a { color: var(--white); text-decoration: none; font-size: 8.5px; padding: 0 11px; line-height: 40px; border-right: 1px solid #444; }
  .main-nav a:first-child { color: var(--orange); padding-left: 20px; }
  .main-nav a:last-child { border-right: none; }

  /* hero */
  .hero-sky { left: 0; top: 128px; width: 758px; height: 203px; background: linear-gradient(var(--sky-top), var(--sky)); }
  .hero-art { left: 108px; top: 128px; width: 541px; height: 239px;
    background:
      linear-gradient(180deg, rgba(255,255,255,0) 0%, rgba(255,255,255,0) 8%, #e98a4f 14%, #f2b765 34%, #e9a36b 50%, #8fc7b8 64%, #e58a62 78%, #c9b2a6 90%, #d8c3b8 100%);
  }
  .hero-caption { left: 108px; top: 367px; width: 541px; height: 40px; background: var(--dark); display: flex; align-items: center; padding-left: 13px; font-size: 15px; color: var(--white); }
  .hero-caption strong { color: var(--orange); font-weight: 500; margin-right: 5px; }
  .dots { position: absolute; right: 12px; top: 17px; display: flex; gap: 4px; }
  .dots i { width: 6px; height: 6px; border-radius: 50%; background: var(--white); }

  /* welcome */
  .owl-art { left: 240px; top: 437px; width: 84px; height: 94px; border-radius: 45% 45% 40% 40%;
    background: linear-gradient(180deg, #2f2a26 0%, #2f2a26 14%, #e9801f 15%, #f5a030 55%, #c9651a 100%); }
  .register-tag { left: 364px; top: 448px; width: 76px; height: 26px; background: var(--orange); color: var(--white); font-size: 9px; line-height: 26px; padding-left: 10px; transform: rotate(-20deg); border-radius: 3px; }
  .welcome-title { left: 120px; top: 541px; width: 320px; text-align: center; font-size: 29px; font-weight: 400; color: var(--text); line-height: 34px; }
  .welcome-text { left: 135px; top: 583px; width: 292px; text-align: center; font-size: 7.5px; font-weight: 400; line-height: 10.5px; color: var(--muted); }
  .btn { background: var(--orange); color: var(--white); text-align: center; font-size: 8.5px; }
  .read-more { left: 250px; top: 619px; width: 72px; height: 24px; line-height: 24px; }

  .signup { left: 455px; top: 420px; width: 194px; height: 222px; background: var(--dark); border-top: 2px solid var(--orange); padding: 15px 12px 0; }
  .signup .field { height: 27px; border: 1px solid var(--field-border); margin-bottom: 3px; font-size: 7.5px; color: #999; padding: 9px 6px; }
  .signup .field.message { height: 48px; }
  .signup-btn { left: 455px; top: 616px; width: 194px; height: 26px; line-height: 26px; font-size: 11px; }

  /* areas */
  .areas { left: 0; top: 670px; width: 758px; height: 258px; background: var(--soft); border-top: 1px solid var(--line); border-bottom: 1px solid var(--line); }
  .area { top: 700px; width: 164px; text-align: center; }
  .area-photo { width: 164px; height: 164px; border-radius: 50%; border: 1px solid #e2e2e2; }
  .area-label { margin-top: 14px; font-size: 22px; font-weight: 300; color: var(--text); white-space: nowrap; }

  /* newsletter */
  .owl-small { left: 112px; top: 961px; width: 50px; height: 53px; border-radius: 45% 45% 40% 40%;
    background: linear-gradient(180deg, #2f2a26 0%, #2f2a26 14%, #e9801f 15%, #f5a030 55%, #c9651a 100%); }
  .news-title { left: 230px; top: 940px; font-size: 21px; font-weight: 300; color: var(--orange); }
  .news-input { left: 230px; top: 973px; width: 191px; height: 31px; border: 1px solid #ddd; font-size: 8px; color: #aaa; padding: 11px 8px; }
  .news-btn { left: 425px; top: 973px; width: 190px; height: 31px; line-height: 31px; font-size: 8.5px; }

  /* footer */
  .footer { left: 0; top: 1014px; width: 758px; height: 146px; background: var(--dark-2); }
  .col { top: 1040px; }
  .col h4 { font-size: 14px; font-weight: 300; color: var(--orange); margin-bottom: 7px; }
  .col li { list-style: none; font-size: 7px; color: var(--white); line-height: 12px; }
  .divider { top: 1042px; width: 1px; height: 96px; background: #555; }
  .post { display: flex; gap: 8px; margin-bottom: 10px; }
  .post-thumb { width: 28px; height: 28px; border-radius: 50%; background: linear-gradient(#e5b98b, #c98a5c); border: 2px solid #eee; flex: none; }
  .post p { font-size: 7px; line-height: 10px; color: var(--white); width: 100px; }
  .social { display: flex; gap: 7px; }
  .social i { width: 26px; height: 26px; border-radius: 50%; }
  .copyright { left: 0; top: 1171px; width: 758px; text-align: center; font-size: 7px; color: var(--text); }
</style>
</head>
<body>

<header>
  <div class="abs brand"><span class="brand-dot"></span><span class="brand-name">PennaBoschetto</span></div>
  <div class="abs phone">
    <svg width="16" height="16" viewBox="0 0 16 16"><circle cx="8" cy="8" r="7" fill="none" stroke="currentColor" stroke-width="1.4"/><path d="M5.3 4.5l1.4 0 .6 1.8-.9.8a5 5 0 0 0 2.5 2.5l.8-.9 1.8.6v1.4c-3.5.3-6.5-2.7-6.2-6.2z" fill="currentColor"/></svg>
    <span>+0800 555 0192</span>
  </div>
  <div class="abs account">Login<span>|</span>Register</div>
  <div class="abs icon-row">
    <div class="icon-ring"><svg width="12" height="12" viewBox="0 0 12 12"><circle cx="6" cy="4" r="2.3" fill="none" stroke="#f7890c" stroke-width="1.2"/><path d="M1.5 11c.5-2.5 2.3-3.6 4.5-3.6s4 1.1 4.5 3.6" fill="none" stroke="#f7890c" stroke-width="1.2"/></svg></div>
    <div class="icon-ring"><svg width="12" height="12" viewBox="0 0 12 12"><path d="M7 1.5h3.5v9H7M1 6h6.5M5 3.5L7.5 6 5 8.5" fill="none" stroke="#f7890c" stroke-width="1.2"/></svg></div>
    <div class="icon-ring"><span class="pip"></span></div>
    <div class="icon-ring"><span class="pip"></span></div>
    <div class="icon-ring"><span class="pip"></span></div>
  </div>
  <nav class="abs main-nav">
    <a href="#">HOME</a><a href="#">LEARNING</a><a href="#">EXPERIMENTING</a><a href="#">COOKING</a><a href="#">GALLERY</a><a href="#">BLOG</a>
  </nav>
</header>

<section>
  <div class="abs hero-sky"></div>
  <div class="abs hero-art" role="img" aria-label="Illustration of a colourful Italian street with bakery, fruit and fish shop fronts under a blue sky with clouds"></div>
  <div class="abs hero-caption"><strong>PENNABOSCHETTO,</strong> THE TASTE OF KNOWLEDGE.
    <div class="dots"><i></i><i></i><i></i></div>
  </div>
</section>

<section>
  <div class="abs owl-art" role="img" aria-label="Illustrated owl teacher mascot with a graduation cap holding a pencil"></div>
  <div class="abs register-tag">REGISTER</div>
  <h1 class="abs welcome-title">WELCOME VISITORS !</h1>
  <p class="abs welcome-text">Ut wisi enim ad minim veniam, quis nostrud exerci tation ullamcorper suscipit bortis nisl ut aliquip ex ea commodo consequat. Duis autem vel eum iriure dolor in hendrerit in vulputate velit esse molestie consequ.</p>
  <div class="abs btn read-more">READ MORE</div>

  <form class="abs signup">
    <div class="field">NAME</div>
    <div class="field">E-MAIL</div>
    <div class="field">NUMBER</div>
    <div class="field">DATE</div>
    <div class="field message">MESSAGE</div>
  </form>
  <div class="abs btn signup-btn">RIGISTER NOW !</div>
</section>

<section>
  <div class="abs areas"></div>
  <div class="abs area" style="left:111px"><div class="area-photo" role="img" aria-label="Photo of two smiling girls drawing with coloured pencils at a classroom desk" style="background:linear-gradient(160deg,#a9d6ee 0%,#e8c09a 40%,#f1c9a8 55%,#f2d14a 78%,#7cc46a 100%)"></div><div class="area-label">LEARNING</div></div>
  <div class="abs area" style="left:297px"><div class="area-photo" role="img" aria-label="Photo of a child in a chef hat mixing ingredients in a bowl" style="background:linear-gradient(170deg,#6f5a4b 0%,#c9a27c 30%,#f0eeea 55%,#d8d8d8 72%,#b23a2e 100%)"></div><div class="area-label">EXPERIMENTING</div></div>
  <div class="abs area" style="left:483px"><div class="area-photo" role="img" aria-label="Photo of pupils building a molecule model in class" style="background:linear-gradient(170deg,#e9e2d6 0%,#c79a7c 35%,#5b4a42 55%,#b98a6d 72%,#efece8 100%)"></div><div class="area-label">COOKING</div></div>
</section>

<section>
  <div class="abs owl-small" role="img" aria-label="Small illustrated owl teacher mascot"></div>
  <h2 class="abs news-title">NEWSLETTER</h2>
  <div class="abs news-input">ENTER YOUR EMAIL HERE</div>
  <div class="abs btn news-btn">SUBSCRIBE NOW !</div>
</section>

<footer>
  <div class="abs footer"></div>
  <div class="abs col" style="left:110px"><h4>MENU</h4><ul><li>HOME</li><li>LEARNING</li><li>EXPERIMENTING</li><li>COOKING</li><li>GALLERY</li><li>BLOG</li></ul></div>
  <div class="abs divider" style="left:202px"></div>
  <div class="abs col" style="left:240px"><h4>SERVICES</h4><ul><li>LEARNING</li><li>EXPERIMENTING</li><li>COOKING</li><li>LEARNING</li><li>EXPERIMENTING</li><li>COOKING</li></ul></div>
  <div class="abs divider" style="left:341px"></div>
  <div class="abs col" style="left:364px"><h4>BLOG</h4>
    <div class="post"><div class="post-thumb" role="img" aria-label="Blog post thumbnail photo"></div><p>Lorem ipsum dolor sit amet, consectetuer adipiscing elit, sed diam nonummy.</p></div>
    <div class="post"><div class="post-thumb" role="img" aria-label="Blog post thumbnail photo"></div><p>Lorem ipsum dolor sit amet, consectetuer adipiscing elit, sed diam nonummy.</p></div>
  </div>
  <div class="abs divider" style="left:519px"></div>
  <div class="abs col" style="left:535px"><h4>SOCIAL</h4>
    <div class="social"><i style="background:#3b5998"></i><i style="background:#3fa9e0"></i><i style="background:#dd4b39"></i></div>
  </div>
  <p class="abs copyright">PENNABOSCHETTO © 2014. ALL RIGHT RESERVED.</p>
</footer>

</body>
</html>
```